Country music artist need a cd cover design. 4 page digipak.

The music is a mix between old school country music, and more of a "Adult oriented Rock"-sound.
The artist name is Torvald Brenke,
I am recording without a record company and the track listing is not 100% set yet, but this is the current order:
1. Waiting On Quiet Rivers
(Brenke, Lindqvar)
2. Under Amber Sky
(Brenke)
3. Hold Steady
(Brenke)
4. Marla, Come Home
(Brenke)
5. Nothing Plain
(Brenke)
6. Pull The Curtain And Stop The Reel
(Brenke, Hävring)
7. Every Mile Just Brought Me Closer Home
(Brenke)
8. Once The Tide Turns Round (2004 version)
(Brenke)
9. Shake The Porch (Live at Café Lindmor)
(Brenke, Dolk)
10. Ya Need The Dust To Find The Rain (Live at Café Lindmor)
(Pruett, Canfel, Marabuni, Tolvin)
Guest musicians:
2, 7: Mr Dale of Prairiedub, Pedal Steel. 3: Anders Pelkvist, Mandolin. 6: Nils Hävring, Drums, Electric guitar & electric Auto Harp. 9 & 10: Bertil Vrandqvist, Drums, Staffan Ek, Electric guitar, Gustaf Renholm, Acoustic guitar & Vocals, Rickard Tylgren, Upright Bass.
Mixied & produced by Torvald Brenke,
Mastered by Carl Benning at Quarry Sound, Nashville, TN.
www.brenketunes.example
https://www.facebook.com/brenketunes
(c) 2017 Brenketunes, All Rights Reserved
International record buying adults
School

```html
<!DOCTYPE html>
<html lang="en">
<head>
<meta charset="utf-8">
<title>Torvald Brenke – Digipak Cover</title>
<link rel="stylesheet" href="https://fonts.googleapis.com/css2?family=Squada+One&display=swap">
<style>
  :root {
    --stage: #2a2a2a;
    --sleeve: #0b0706;
    --cream: #e9e0d4;
    --cream-soft: #d8cdbf;
    --label-red: #ff1a1a;
    --photo-dark: #0e0907;
    --photo-curtain: #1c1410;
    --photo-mid: #3a2a20;
    --photo-warm: #8a7260;
    --photo-light: #cdbba6;
  }
  * { margin: 0; padding: 0; box-sizing: border-box; }
  html, body {
    width: 1200px; height: 1000px; overflow: hidden;
    background: var(--stage);
    font-family: "Squada One", "Arial Narrow", sans-serif;
  }
  .sleeve {
    position: absolute; left: 30px; top: 202px;
    width: 1150px; height: 576px;
    background: var(--sleeve);
  }
  .back-photo {
    position: absolute; left: 130px; top: 80px;
    width: 400px; height: 360px;
    opacity: 0.55;
    background:
      radial-gradient(ellipse 70px 90px at 68% 22%, rgba(205,187,166,0.55) 0%, rgba(205,187,166,0) 100%),
      radial-gradient(ellipse 150px 70px at 45% 28%, rgba(58,42,32,0.9) 0%, rgba(58,42,32,0) 100%),
      radial-gradient(ellipse 90px 110px at 22% 50%, rgba(138,114,96,0.6) 0%, rgba(138,114,96,0) 100%),
      radial-gradient(ellipse 190px 140px at 55% 85%, rgba(42,30,23,0.9) 0%, rgba(42,30,23,0) 100%);
  }
  .tracklist {
    position: absolute; left: 39px; top: 30px;
    list-style: none; color: var(--cream);
  }
  .track { height: 48.2px; }
  .track-title {
    display: block; font-size: 21px; line-height: 18px;
    letter-spacing: 0.6px; text-transform: uppercase;
  }
  .track-credit {
    display: block; font-size: 18px; line-height: 15px;
    letter-spacing: 0.4px; color: var(--cream-soft); text-transform: uppercase;
  }
  .spine-title {
    position: absolute; left: 555px; top: 148px;
    writing-mode: vertical-rl;
    font-size: 30px; letter-spacing: 1.5px;
    color: var(--cream); text-transform: uppercase;
  }
  .front-photo {
    position: absolute; left: 615px; top: 45px;
    width: 498px; height: 451px;
    background:
      radial-gradient(ellipse 60px 110px at 17% 30%, var(--photo-light) 0%, rgba(205,187,166,0) 100%),
      radial-gradient(ellipse 80px 120px at 64% 45%, rgba(205,187,166,0.7) 0%, rgba(205,187,166,0) 100%),
      radial-gradient(ellipse 190px 85px at 50% 25%, var(--photo-mid) 0%, rgba(58,42,32,0) 100%),
      radial-gradient(ellipse 230px 170px at 52% 80%, rgba(58,42,32,0.85) 0%, rgba(58,42,32,0) 100%),
      radial-gradient(ellipse 60px 70px at 8% 55%, rgba(138,114,96,0.7) 0%, rgba(138,114,96,0) 100%),
      linear-gradient(90deg, var(--photo-dark) 0%, var(--photo-curtain) 50%, var(--photo-dark) 100%);
  }
  .artist-name {
    position: absolute; left: 843px; top: 26px;
    transform: translateX(-50%); white-space: nowrap;
    font-size: 46px; font-weight: 400; letter-spacing: 2px;
    color: var(--cream); text-transform: uppercase;
  }
  .panel-label {
    position: absolute; top: 534px;
    font-size: 35px; letter-spacing: 1.2px;
    color: var(--label-red); text-transform: uppercase;
  }
  .panel-label--back { left: 170px; }
  .panel-label--front { left: 844px; }
</style>
</head>
<body>
  <section class="sleeve">
    <div class="back-photo" role="img" aria-label="Faded portrait of the artist in a cowboy hat behind the track list"></div>
    <ol class="tracklist">
      <li class="track"><span class="track-title">1. Waiting On Quiet Rivers</span><span class="track-credit">(Brenke, Lindqvar)</span></li>
      <li class="track"><span class="track-title">2. Under Amber Sky</span><span class="track-credit">(Brenke)</span></li>
      <li class="track"><span class="track-title">3. Hold Steady</span><span class="track-credit">(Brenke)</span></li>
      <li class="track"><span class="track-title">4. Marla, Come Home</span><span class="track-credit">(Brenke)</span></li>
      <li class="track"><span class="track-title">5. Nothing Plain</span><span class="track-credit">(Brenke)</span></li>
      <li class="track"><span class="track-title">6. Pull The Curtain And Stop The Reel</span><span class="track-credit">(Brenke, Hävring)</span></li>
      <li class="track"><span class="track-title">7. Every Mile Just Brought Me Closer Home</span><span class="track-credit">(Brenke)</span></li>
      <li class="track"><span class="track-title">8. Once The Tide Turns Round (2004 Version)</span><span class="track-credit">(Brenke)</span></li>
      <li class="track"><span class="track-title">9. Shake The Porch (Live at Café Lindmor)</span><span class="track-credit">(Brenke, Dolk)</span></li>
      <li class="track"><span class="track-title">10. Ya Need The Dust To Find The Rain (Live at Café Lindmor)</span><span class="track-credit">(Pruett, Canfel, Marabuni, Tolvin)</span></li>
    </ol>
    <div class="spine-title">Torvald Brenke</div>
    <div class="front-photo" role="img" aria-label="Sepia portrait of the artist tipping a cowboy hat, head bowed, against a dark curtain"></div>
    <h1 class="artist-name">Torvald Brenke</h1>
    <p class="panel-label panel-label--back">Back Cover</p>
    <p class="panel-label panel-label--front">Front Cover</p>
  </section>
</body>
</html>
```